Waterjet Cutting Business requires an up to date website

We currently have a website which is outdated and in need of modernization.
We are only looking for a simple website with around 4 pages: Home, Contact Us, Materials, Gallery.
We have some pictures and a logo which can be used.
Our primary business is profile cutting of materials to customers specifications using high-pressure water with abrasive.
We are looking for creative ideas and are open to suggestions!
http://brimfieldcutworks.com/index.asp?pid=1
Update:
Cut quality picture (uploaded)
Map
Comparison to other profile cutting methods such as plasma/laser
Single page style without continuous scrolling
"We can cut virtually any material from any drawing whether it be a Full 3D cad models to hand sketched "
Target Market(s)
Film Industry, Prototype, Engineering, Architect, Artisits, one off designs
Industry/Entity Type
Engineering
Number of Pages Required
1 page
Font styles to use
Look and feel

```html
<!DOCTYPE html>
<html lang="en">
<head>
<meta charset="utf-8">
<title>Brimfield Cutworks – Waterjet Cutting Service</title>
<link href="https://fonts.googleapis.com/css2?family=Open+Sans:wght@400;600;700&display=swap" rel="stylesheet">
<style>
:root{
  --orange:#f47b20;
  --blue:#1a86c8;
  --blue-dark:#1574b3;
  --text:#333;
  --muted:#555;
  --light-blue:#cfe6f5;
  --line:#e3e3e3;
  --white:#fff;
}
*{margin:0;padding:0;box-sizing:border-box}
html,body{width:1160px;height:1200px;overflow:hidden;background:#fff}
body{font-family:"Open Sans",Arial,sans-serif;color:var(--text);position:relative}
.hero{position:absolute;left:0;top:0;width:1160px;height:435px;
  background:radial-gradient(ellipse at 58% 50%,#d9d4cc 0%,#8a837b 35%,#4b4540 70%,#2d2925 100%)}
.hero-rule{position:absolute;left:0;top:80px;width:1160px;height:1px;background:rgba(255,255,255,.55)}
.brand{position:absolute;top:22px;width:100%;text-align:center;color:#fff;font-size:34px;font-weight:700;letter-spacing:6px;text-transform:uppercase}
.hero-title{position:absolute;top:180px;width:100%;text-align:center;color:#fff;font-size:19px;font-weight:600}
.hero-sub{position:absolute;top:213px;left:300px;width:560px;text-align:center;color:#fff;font-size:15px;line-height:22px}
.btn{position:absolute;top:276px;left:526px;width:108px;height:29px;border-radius:15px;background:var(--orange);color:#fff;font-size:11px;font-weight:600;text-align:center;line-height:29px}
.card{position:absolute;top:399px;width:254px;height:304px;background:#fff;border-radius:4px;box-shadow:0 2px 12px rgba(0,0,0,.12);overflow:hidden}
.card-photo{height:163px}
.card-stripe{height:3px;background:var(--blue-dark)}
.card.active .card-stripe{background:var(--orange)}
.card p{margin:17px 22px 0;text-align:center;font-size:10.5px;line-height:22.5px;color:var(--muted)}
.card .more{position:absolute;top:265px;width:100%;text-align:center;font-size:9.5px;font-weight:700;color:var(--blue)}
.card.active .more{color:var(--orange)}
.nav-item{position:absolute;top:716px;width:254px;text-align:center;font-size:19px;color:var(--blue)}
.nav-item::after{content:"";display:block;width:26px;height:2px;background:var(--blue);margin:4px auto 0}
.nav-item.active{color:var(--orange)}
.nav-item.active::after{background:var(--orange)}
.quality-rule{position:absolute;top:838px;left:0;width:1160px;height:1px;background:var(--line)}
.grade{position:absolute;top:791px;width:140px;text-align:center}
.grade-thumb{width:93px;height:93px;margin:0 auto;background:#fff;border-radius:4px;box-shadow:0 1px 5px rgba(0,0,0,.25);padding:5px;position:relative}
.grade-photo{width:100%;height:100%;background:linear-gradient(135deg,#9c9c9c,#777 50%,#8e8e8e)}
.grade-code{position:absolute;top:4px;width:100%;left:0;text-align:center;color:rgba(255,255,255,.85);font-size:24px}
.grade-name{margin-top:8px;font-size:11.5px;line-height:17.5px;color:var(--text)}
.grade-note{font-size:11.5px;line-height:17.5px;color:var(--orange)}
.contact{position:absolute;top:1001px;left:0;width:580px;height:160px;background:var(--light-blue)}
.field{position:absolute;left:144px;width:156px;border-bottom:1px solid #557a99;font-size:9px;color:#667;padding-bottom:4px}
.send{position:absolute;left:145px;top:119px;width:35px;height:13px;border-radius:7px;background:var(--blue-dark);color:#fff;font-size:7px;font-weight:700;text-align:center;line-height:13px}
.contact h3{position:absolute;left:421px;top:33px;font-size:11.5px;font-weight:600;color:var(--blue-dark)}
.info{position:absolute;left:421px;font-size:9px;line-height:14px;color:#444;display:flex;gap:8px}
.map{position:absolute;top:1001px;left:580px;width:580px;height:160px;background:linear-gradient(120deg,#eceae6,#f4f2ee 60%,#ebe7df)}
.callout{position:absolute;top:1009px;left:782px;width:176px;height:57px;background:var(--orange);color:#fff;font-size:7.8px;line-height:16px;text-align:center;padding-top:4px;border-radius:2px}
.callout::after{content:"";position:absolute;left:82px;bottom:-7px;border:6px solid transparent;border-top-color:var(--orange);border-bottom:0}
.footer{position:absolute;top:1161px;left:0;width:1160px;height:39px;background:var(--blue)}
.copy{position:absolute;left:144px;top:13px;font-size:9.5px;color:#fff}
.copy span{color:var(--orange)}
.social{position:absolute;right:154px;top:13px;display:flex;gap:13px}
.social i{width:13px;height:13px;border-radius:50%;background:#fff;display:block}
.social i:nth-child(2){background:var(--orange)}
</style>
</head>
<body>
<header class="hero" role="img" aria-label="Photo of a waterjet cutting head spraying water and sparks">
  <div class="brand">Brimfield Cutworks</div>
  <div class="hero-rule"></div>
  <h1 class="hero-title">WATERJET CUTTING SERVICE</h1>
  <p class="hero-sub">We can cut virtually any material from any drawing whether it be a Full 3D cad models to hand sketched.</p>
  <div class="btn">Contact Us</div>
</header>

<div class="card" style="left:145px">
  <div class="card-photo" role="img" aria-label="Waterjet nozzle over a teal cutting grid" style="background:linear-gradient(160deg,#0a0f12,#123b3a 60%,#1a8a84)"></div>
  <div class="card-stripe"></div>
  <p>We can cut virtually any material from any drawing whether it be a Full 3D cad models to hand sketched.......</p>
  <div class="more">Read more</div>
</div>
<div class="card active" style="left:453px">
  <div class="card-photo" role="img" aria-label="Cutting head lit in magenta light over a work grid" style="background:linear-gradient(160deg,#2a0c5a,#b0208e 55%,#e23aa8)"></div>
  <div class="card-stripe"></div>
  <p>It is possible to cut virtually any profile in any material with waterjet.Materials we can cut .....</p>
  <div class="more">Read more</div>
</div>
<div class="card" style="left:761px">
  <div class="card-photo" role="img" aria-label="Waterjet head cutting a perforated metal sheet" style="background:linear-gradient(160deg,#2b3650,#5d6470 50%,#2a2a2d)"></div>
  <div class="card-stripe"></div>
  <p>By combining our technical expertise with Hydrona's latest dynamic head waterjet technology we are able to offer......</p>
  <div class="more">Read more</div>
</div>

<nav>
  <div class="nav-item" style="left:145px">HOME</div>
  <div class="nav-item active" style="left:453px">MATERIALS</div>
  <div class="nav-item" style="left:761px">GALLERY</div>
</nav>

<div class="quality-rule"></div>
<section>
  <div class="grade" style="left:121px"><div class="grade-thumb"><div class="grade-photo" role="img" aria-label="Close-up of a rough separation cut edge"></div><div class="grade-code">Q1</div></div><div class="grade-name">Seperation<br>Cut</div></div>
  <div class="grade" style="left:315px"><div class="grade-thumb"><div class="grade-photo" role="img" aria-label="Close-up of a through cut edge"></div><div class="grade-code">Q2</div></div><div class="grade-name">Through<br>Cut</div></div>
  <div class="grade" style="left:508px"><div class="grade-thumb"><div class="grade-photo" role="img" aria-label="Close-up of a clean cut edge"></div><div class="grade-code">Q3</div></div><div class="grade-name">Clean Cut</div><div class="grade-note">Typically closer<br>than<br>+/_ 0.010”</div></div>
  <div class="grade" style="left:701px"><div class="grade-thumb"><div class="grade-photo" role="img" aria-label="Close-up of a good edge finish"></div><div class="grade-code">Q4</div></div><div class="grade-name">Good Edge<br>FInish</div></div>
  <div class="grade" style="left:895px"><div class="grade-thumb"><div class="grade-photo" role="img" aria-label="Close-up of an excellent edge finish"></div><div class="grade-code">Q5</div></div><div class="grade-name">Excellent Edge<br>Finish</div><div class="grade-note">Typically Closer<br>than +/_ 0.005”</div></div>
</section>

<section class="contact">
  <div class="field" style="top:32px">Name:</div>
  <div class="field" style="top:61px">Email:</div>
  <div class="field" style="top:90px">How can we help?<svg style="position:absolute;right:0;top:3px" width="6" height="5"><path d="M0 0h6L3 5z" fill="#f47b20"/></svg></div>
  <div class="send">Send</div>
  <h3>CONTACT US</h3>
  <div class="info" style="top:56px"><svg width="17" height="17" viewBox="0 0 17 17"><circle cx="8.5" cy="8.5" r="7.5" fill="none" stroke="#1574b3" stroke-width="1.2"/><path d="M6 5c-1 1-.5 3 1.5 5s4 2.5 5 1.5l-1.5-1.5-1 .7c-1-.5-2-1.5-2.5-2.5l.7-1z" fill="#1574b3"/></svg><div>Phone Number<br>01632 960482</div></div>
  <div class="info" style="top:96px"><svg width="17" height="13" viewBox="0 0 17 13"><rect x=".6" y=".6" width="15.8" height="11.8" fill="none" stroke="#1574b3" stroke-width="1.2"/><path d="M.6.6l7.9 6.5L16.4.6M.6 12.4l5.8-5.3M16.4 12.4l-5.8-5.3" fill="none" stroke="#1574b3" stroke-width="1.2"/></svg><div>Email<br>info@brimfieldcutw<br>orks.com</div></div>
</section>
<div class="map" role="img" aria-label="Street map showing the workshop location on a business park"></div>
<div class="callout">Unit 7, Kestrel Court, Marlow Lane,<br>Ashgrove Trade Park, Brimfield, Hants,<br>BF4 2QT</div>
<svg style="position:absolute;left:860px;top:1078px" width="20" height="28" viewBox="0 0 20 28"><path d="M10 0C4.5 0 1 4 1 9c0 6 9 19 9 19s9-13 9-19c0-5-3.5-9-9-9z" fill="#e53935"/><circle cx="10" cy="9" r="3" fill="#8b1010"/></svg>

<footer class="footer">
  <div class="copy"><span>©</span> Brimfield Cutworks 2018. All rights reserved.</div>
  <div class="social"><i></i><i></i><i></i><i></i></div>
</footer>
</body>
</html>
```